Wordpress Design Project - Vibrant Children's school bag website

We need a fresh design for the landing page of our new web site and blog: tumblewickshop.com

Tumblewick specialises in supplying schools all over the world and now also parents directly with, personalised school bags, accessories, crafts and gifts for their children.

I have attached the visual that our web designers have provided so that we can see the layout of the various window, but now we need to add the personal touch of making it our own and visually making the site look enticing and exciting to shop on.

Hello Designers,

We are now in the final round of choosing a design.  We have found that most deisgns are very similar and that none are completley original.  Therefore, we are willing to throw our wire frame away and start with a compleltely new visual so you can design what ever you like!

The only requirements we have is that we must have:
- A large rolling banner to show our products lines
- Our Company logo
- Meta going tags across the top
- Icons for facebook,pintrest,blog,
- Account Login bar
- A log in area for schools
- A login area to register for the Club Tumbo

So we are looking for something that really stands out from the crowd!

can you deliver?

Thanks,

Target Market(s)

To appeal to mum's shopping on line for their children's school items and gifts.

Industry/Entity Type

School

Requirements
Must have
• -When you see the visual attached please note the amendments:
- the word 'school bags' under our company name will not appear
- the tag line "Australia's no 1 specialist school bag company' should be deleted. We will leave this area open so that you can include some simple icons that we would like featured across the top of the banner i.e:
- a love heart icon + wording to say : Made with love
- A 'delivery' icon + wording to say : Free delivery
- A 'warranty' icon + wording to say : up to 25 year warranty
- A 'world' icon + wording to say : we ship to the universe
(Please see: www.plumcottage.com.au for reference of what we mean!)

We we want the overall design to be clean, fresh, crisp and fun to look at.

You may alter the colours of everything, even the coloured tabs. we think that the coloured tabs should actually just be one colour through out and to let the tumblewick name stand out with all it's.

The top/main photo will be a rolling banner.

You can change the shapes of the boxes but keep to the wire frame.

Please alter the design of the black/coloured club tumbo card to suit your design.

Our aim is to also change the side panels in peak seasons to reflect halloween banner, christmas banner etc.

Please see my screen shot of the current page and see where the "dots' pattern sits on either side of the shopping panels. Please include the side panels as we want to change the design to have themes i.e for halloween, for christmas etc etc.

example of websites that have this:

http://www.reefmarlo.com/

Please include a 'blog' and pintrest icon.

The site will not only manage our retail sales but will also be a portal for our schools to register and place their bulk orders with us. So the "wholesale register box" must stand out so our school customers can easily see where they need to click & register.
Should not have
• Please do not do a 'baby' boutique theme. We need a theme that appeals to mum's that have children across the ages of 3-14 years.

```html
<!DOCTYPE html>
<html lang="en">
<head>
<meta charset="utf-8">
<title>Tumblewick – School Bags &amp; Gifts</title>
<link href="https://fonts.googleapis.com/css2?family=Arimo:wght@400;700&family=Dosis:wght@600;700&family=Fredoka:wght@600&display=swap" rel="stylesheet">
<style>
:root{
  --green:#8cc22a; --green-dark:#6fa31a;
  --orange:#f7a21b; --orange-dark:#e8860a;
  --blue:#15a8e6; --blue-dark:#0a8fd0;
  --pink:#e4157a;
  --wood:#e3dbd0; --wood-line:#d6cdc0;
  --panel:#efefef; --white:#ffffff;
  --text:#444; --muted:#666;
  --frame:#e9b764; --frame-dark:#c98e3a;
  --footer:#c6bcaf;
}
*{box-sizing:border-box;margin:0;padding:0}
html,body{width:1159px;height:1200px;overflow:hidden}
body{position:relative;font-family:"Arimo",Arial,sans-serif;color:var(--text);
  background:repeating-linear-gradient(90deg,var(--wood) 0 7px,var(--wood-line) 7px 8px,var(--wood) 8px 13px);}
.abs{position:absolute}
.header{left:0;top:0;width:1159px;height:156px;background:linear-gradient(#9ccd33,var(--green))}
.logo-card{left:83px;top:19px;width:332px;height:118px;background:var(--white);border-radius:10px;box-shadow:2px 3px 0 var(--green-dark)}
.logo-inner{position:absolute;left:12px;top:12px;right:12px;bottom:12px;border:1px solid #e3e3e3;border-radius:8px;display:flex;align-items:center;justify-content:center;gap:10px;box-shadow:0 2px 4px rgba(0,0,0,.15)}
.logo-name{font-family:"Fredoka",sans-serif;font-weight:600;font-size:46px;color:var(--blue)}
.logo-dot{width:14px;height:14px;border-radius:50%;background:var(--pink)}
.top-links{left:865px;top:19px;width:210px;height:28px;background:var(--white);font-size:12px;color:#222;display:flex;align-items:center;justify-content:center;gap:6px}
.social{left:897px;top:59px;display:flex;gap:5px}
.social span{width:32px;height:32px;border-radius:2px;border:1px solid rgba(0,0,0,.2)}
.cart{left:832px;top:103px;width:243px;height:37px;background:var(--white);font-size:12px;display:flex;align-items:center;padding-left:10px;gap:8px;color:#222}
.cart b{color:var(--pink)}
.checkout{background:var(--blue);color:#111;font-size:11px;padding:3px 8px;margin-left:4px}
.nav{left:84px;top:175px;width:991px;height:41px;background:linear-gradient(#ffb43a,var(--orange-dark));border-radius:3px;display:flex;align-items:center;padding-left:11px}
.nav a{font-family:"Arimo",Arial,sans-serif;font-weight:700;font-size:13px;color:var(--white);text-decoration:none;padding:0 11px;height:41px;line-height:41px;border-right:1px solid rgba(255,255,255,.35);text-shadow:0 1px 1px rgba(0,0,0,.3)}
.nav a.active{background:linear-gradient(#36bff0,var(--blue-dark));height:49px;margin-top:-8px;line-height:55px;border-radius:4px 4px 0 0;border:none}
.banner-frame{left:84px;top:229px;width:991px;height:377px;background:linear-gradient(135deg,#f3c57a,var(--frame),var(--frame-dark));border:1px solid #b98536}
.banner-photo{left:110px;top:257px;width:938px;height:322px;background:linear-gradient(180deg,#3d5a2e,#7c8f6a 45%,#9fa9b8 75%,#8d8a7e)}
.dots{left:543px;top:559px;display:flex;gap:10px}
.dots i{width:11px;height:11px;background:#333}
.dots i:first-child{background:var(--blue)}
.bag-photo{left:2px;top:343px;width:265px;height:278px;border-radius:40% 40% 12% 12%;background:linear-gradient(135deg,#e6e8ec,#8a8c94 55%,#e8c41a 56%,#b89810)}
.card{top:639px;width:296px;height:211px;background:var(--white);padding:7px;box-shadow:0 1px 2px rgba(0,0,0,.15)}
.card-body{position:relative;height:100%;background:var(--panel);padding:8px 11px 8px 14px}
.card h2{font-family:"Dosis",sans-serif;font-weight:700;font-size:25px;color:var(--blue);line-height:28px}
.who{font-size:13px;font-weight:700;color:#222;margin-top:2px}
.role{font-size:12px;color:#222}
.quote{font-size:10.4px;line-height:16px;color:var(--muted);margin-top:12px;text-align:justify}
.portrait{float:right;margin:2px 0 6px 10px;width:72px;height:93px;background:var(--white);border:1px solid #ddd;padding:4px}
.portrait div{width:100%;height:100%;background:linear-gradient(#c9b9a6,#8fa2b8)}
.tab-btn{position:absolute;left:20px;bottom:-7px;background:linear-gradient(#fbaa2a,var(--orange-dark));color:var(--white);font-weight:700;font-size:12px;padding:8px 16px;border-radius:4px 4px 0 0}
.tab-btn::after{content:" ▸";font-size:10px}
.club p{font-size:14px;font-weight:700;color:#222;line-height:18px;margin-top:4px}
.club label{display:block;font-size:12px;font-weight:700;color:var(--muted);margin-top:18px}
.field{background:var(--white);border:1px solid #ddd;height:24px}
.boy-photo{position:absolute;right:6px;top:18px;width:110px;height:186px;border-radius:40px 40px 6px 6px;background:linear-gradient(#e8c9aa,#5c86b4 45%,#3b4f6e)}
.panel{top:885px;height:246px;background:var(--white);box-shadow:0 1px 2px rgba(0,0,0,.12)}
.ribbon{top:875px;height:34px;font-family:"Dosis",sans-serif;font-weight:700;font-size:22px;color:var(--white);padding-left:14px;line-height:34px;text-shadow:0 1px 1px rgba(0,0,0,.25);clip-path:polygon(0 0,calc(100% - 22px) 0,100% 50%,calc(100% - 22px) 100%,0 100%)}
.video-still{left:99px;top:924px;width:224px;height:194px;background:linear-gradient(#5b3a34,#3d2e2e 60%,#2a2a2a)}
.play{left:178px;top:990px;width:64px;height:64px;border-radius:50%;background:rgba(60,55,55,.85)}
.play::after{content:"";position:absolute;left:25px;top:18px;border-left:22px solid #bbb;border-top:14px solid transparent;border-bottom:14px solid transparent}
.controls{left:99px;top:1104px;width:224px;height:14px;background:#222}
.controls i{position:absolute;left:16px;top:6px;width:175px;height:2px;background:#888}
.post{padding:12px 14px 10px;border-bottom:1px solid #ddd;margin:0 8px 0 0}
.post h3{font-size:12px;font-weight:700;color:#333}
.post p{font-size:10.6px;line-height:16px;color:var(--muted);margin-top:4px}
.post .meta{display:flex;justify-content:space-between;font-size:12px;font-weight:700;color:#333;margin-top:3px}
.reg label{display:block;font-size:12px;font-weight:700;color:#333;margin:14px 0 6px}
.reg .field{height:25px}
.btn{display:inline-block;background:linear-gradient(#fbaa2a,var(--orange-dark));color:var(--white);font-size:12px;font-weight:700;padding:7px 12px;border-radius:2px;margin-top:12px}
.footer{left:0;top:1152px;width:1159px;height:48px;background:var(--footer);font-size:12px;color:#333;text-align:center;line-height:48px}
</style>
</head>
<body>
<header class="header abs"></header>
<div class="logo-card abs"><div class="logo-inner"><span class="logo-name">tumblewick</span><span class="logo-dot"></span></div></div>
<div class="top-links abs"><span>Account Login</span>|<span>Blog</span>|<span>Contact Us</span></div>
<div class="social abs" aria-label="Social links">
  <span style="background:#f08a1e"></span><span style="background:#1a75b3"></span><span style="background:#5fc6ea"></span><span style="background:#3b5b9d"></span><span style="background:#cb2027"></span>
</div>
<div class="cart abs">
  <svg width="20" height="18" viewBox="0 0 20 18"><path d="M1 2h3l2 9h10l2-7H5" fill="none" stroke="#e4157a" stroke-width="2"/><circle cx="8" cy="15" r="1.6" fill="#e4157a"/><circle cx="15" cy="15" r="1.6" fill="#e4157a"/></svg>
  <span>Add to Cart <b>($ 150,00)</b></span><span class="checkout">Checkout</span>
</div>
<nav class="nav abs">
  <a class="active">Test menu</a><a>Kids Backpacks</a><a>Kids Bags</a><a>Sports</a><a>Kids Clothing</a><a>Art &amp; Craft</a><a>Music</a><a>Kids Diaries</a><a>Kids Storage</a><a>Extra Stuff</a><a style="border:none">Sale</a>
</nav>
<div class="banner-frame abs"></div>
<div class="banner-photo abs" role="img" aria-label="Rolling banner photo of school children running with backpacks"></div>
<div class="dots abs"><i></i><i></i><i></i><i></i></div>
<div class="bag-photo abs" role="img" aria-label="Product photo of school backpacks with books"></div>

<section class="card abs" style="left:88px"><div class="card-body">
  <h2>Endorsements</h2>
  <div class="portrait"><div role="img" aria-label="Portrait of the endorsing doctor"></div></div>
  <div class="who">Dr Lewis Marrin</div><div class="role">Chiropractor &amp; Osteopath</div>
  <p class="quote">“Choosing the correct backpack for your child to start the school year with is an important decision for any parent to make. Importantly, your school backpack should be ergonomic and light to carry..”</p>
  <span class="tab-btn">Read More</span></div></section>
<section class="card abs" style="left:431px"><div class="card-body">
  <h2>Endorsements</h2>
  <div class="portrait"><div role="img" aria-label="Portrait of the endorsing doctor"></div></div>
  <div class="who">Dr Lewis Marrin</div><div class="role">Chiropractor &amp; Osteopath</div>
  <p class="quote">“Choosing the correct backpack for your child to start the school year with is an important decision for any parent to make. Importantly, your school backpack should be ergonomic and light to carry..”</p>
  <span class="tab-btn">Read More</span></div></section>
<section class="card club abs" style="left:774px"><div class="card-body">
  <h2>Club tumbo</h2><p>join now for 15% off<br>your first order!</p>
  <label>Enter your Email</label><div class="field" style="width:146px"></div>
  <div class="boy-photo" role="img" aria-label="Photo of a boy carrying a school backpack"></div>
  <span class="tab-btn">Join Now</span></div></section>

<div class="panel abs" style="left:84px;width:253px"></div>
<div class="ribbon abs" style="left:84px;width:274px;background:linear-gradient(#3cc4f5,var(--blue-dark))">Video</div>
<div class="video-still abs" role="img" aria-label="Video still of two girls sitting on a bench"></div>
<div class="play abs"></div>
<div class="controls abs"><i></i></div>

<div class="panel abs" style="left:377px;width:392px;padding-top:34px">
  <div class="post"><h3>Lorem Ipsum is simply</h3><p>Lorem Ipsum is simply dummy text of the printing and typesetting industry. Lorem Ipsum has been the industry's standard dummy text ever since the 1500s, when an unknown printer took a galley of type.</p><div class="meta"><span>6 Sepember, 2012</span><span>Read More ▸</span></div></div>
  <div class="post" style="border:none"><h3>Lorem Ipsum is simply</h3><p>Lorem Ipsum is simply dummy text of the printing and typesetting industry. Lorem Ipsum has been the industry's standard dummy text ever since the 1500s, when an unknown printer took a galley of type.</p><div class="meta"><span>6 Sepember, 2012</span><span>Read More ▸</span></div></div>
</div>
<div class="ribbon abs" style="left:377px;width:413px;background:linear-gradient(#fbb03a,var(--orange-dark))">Blog</div>

<div class="panel reg abs" style="left:809px;width:245px;padding:34px 14px 0">
  <label>First Name:</label><div class="field"></div>
  <label>Last Name:</label><div class="field"></div>
  <label>Email Address:</label><div class="field"></div>
  <span class="btn">Register</span>
</div>
<div class="ribbon abs" style="left:809px;width:266px;background:linear-gradient(#95cf2c,var(--green-dark))">Registration</div>

<footer class="footer abs">© 2009 Tumblewick. All rights reserved</footer>
</body>
</html>
```